product development company BRVENKO LLC business card

We need a business card design for a company based in Texas called 'BRVENKO LLC'. Our first product is a illuminated portable ice chest that is called ' Pebble Drift coolers'. Pebble drift coolers is trademarked. I would like to have the pebble drift trademark somewhere on the card as well as the BRVENKO LLC name.

Target Market(s)

outdoor industry

Industry/Entity Type

Business

Contact Information for Business Card

i would like to have BRVENKO LLC logo larger than the Pebble drift coolers logo.

Font styles to use
Serif
Sans Serif

```html
<!DOCTYPE html>
<html lang="en">
<head>
<meta charset="utf-8">
<title>BRVENKO LLC – Business Card</title>
<link href="https://fonts.googleapis.com/css2?family=Cinzel:wght@500&family=Arimo:wght@400;700&display=swap" rel="stylesheet">
<style>
  :root {
    --bg: #e2dbda;
    --ink: #111111;
    --card-dark: #000000;
    --card-light: #ffffff;
    --text-light: #ffffff;
    --rule: #333333;
  }
  html, body {
    margin: 0;
    padding: 0;
    width: 1200px;
    height: 1000px;
    overflow: hidden;
    background: var(--bg);
  }
  .canvas {
    position: relative;
    width: 1200px;
    height: 1000px;
  }
  .card {
    position: absolute;
    left: 295px;
    width: 610px;
    border-radius: 22px;
    overflow: hidden;
  }
  .card--front {
    top: 140px;
    height: 347px;
    background: var(--card-dark);
    color: var(--text-light);
  }
  .card--back {
    top: 524px;
    height: 344px;
    background: var(--card-light);
    color: var(--ink);
  }
  .wordmark {
    font-family: "Cinzel", serif;
    font-weight: 500;
    text-align: center;
    line-height: 1;
  }
  .card--front .wordmark {
    position: absolute;
    left: 0;
    right: 0;
    top: 140px;
  }
  .wordmark__name {
    display: block;
    font-size: 62px;
    letter-spacing: 1px;
  }
  .wordmark__suffix {
    display: block;
    font-size: 28px;
    letter-spacing: 12px;
    margin-top: 8px;
    padding-left: 12px;
  }
  .card--back .wordmark {
    position: absolute;
    left: 24px;
    top: 36px;
    width: 268px;
  }
  .card--back .wordmark__name { font-size: 36px; }
  .card--back .wordmark__suffix { font-size: 18px; letter-spacing: 8px; margin-top: 4px; padding-left: 8px; }
  .product-mark {
    position: absolute;
    right: 28px;
    top: 50px;
    display: flex;
    align-items: center;
    gap: 7px;
    font-family: "Arimo", sans-serif;
    font-weight: 700;
    font-size: 13px;
    color: var(--ink);
  }
  .product-mark__square {
    width: 18px;
    height: 18px;
    background: var(--ink);
  }
  .holder {
    position: absolute;
    right: 27px;
    top: 178px;
    text-align: right;
    font-family: "Arimo", sans-serif;
  }
  .holder__name {
    font-weight: 700;
    font-size: 21px;
    font-variant: small-caps;
    letter-spacing: 0.5px;
  }
  .holder__role {
    font-size: 15px;
    letter-spacing: 2px;
    margin-top: 4px;
  }
  .divider {
    position: absolute;
    left: 18px;
    right: 17px;
    top: 242px;
    border-top: 3px dotted var(--rule);
  }
  .contact {
    position: absolute;
    top: 264px;
    font-family: "Arimo", sans-serif;
    font-size: 15px;
    line-height: 20px;
    list-style: none;
    margin: 0;
    padding: 0;
  }
  .contact--left { left: 33px; }
  .contact--right { left: 229px; }
  .contact__item {
    display: flex;
    align-items: flex-start;
    gap: 6px;
  }
  .contact__icon {
    width: 14px;
    height: 14px;
    margin-top: 3px;
    flex: none;
    fill: var(--ink);
  }
  .contact__company { font-weight: 700; }
  .contact__indent { padding-left: 20px; }
</style>
</head>
<body>
<div class="canvas">

  <section class="card card--front">
    <div class="wordmark">
      <span class="wordmark__name">BRVENKO</span>
      <span class="wordmark__suffix">LLC</span>
    </div>
  </section>

  <section class="card card--back">
    <div class="wordmark">
      <span class="wordmark__name">BRVENKO</span>
      <span class="wordmark__suffix">LLC</span>
    </div>

    <div class="product-mark">
      <span class="product-mark__square"></span>
      <span>Pebble Drift Coolers</span>
    </div>

    <div class="holder">
      <div class="holder__name">M. Carver Hollis</div>
      <div class="holder__role">DIRECTOR</div>
    </div>

    <div class="divider"></div>

    <ul class="contact contact--left">
      <li class="contact__item">
        <svg class="contact__icon" viewBox="0 0 16 16"><path d="M1 5c0-2 3-3 7-3s7 1 7 3v1h-4V4.5H5V6H1z"/><path d="M4 7h8l2 7H2z"/><circle cx="8" cy="10.5" r="1.6" fill="#fff"/></svg>
        <span>512 555 0148</span>
      </li>
      <li class="contact__item">
        <svg class="contact__icon" viewBox="0 0 16 16"><path d="M4 0h8v16H4z M5.3 2v10h5.4V2z"/><circle cx="8" cy="14" r="0.9" fill="#fff"/></svg>
        <span>512 555 0148</span>
      </li>
      <li class="contact__item">
        <svg class="contact__icon" viewBox="0 0 16 16"><path d="M0 3h16v10H0z"/><path d="M1 4l7 5 7-5" fill="none" stroke="#fff" stroke-width="1.3"/></svg>
        <span>Brvenko@info.com</span>
      </li>
    </ul>

    <ul class="contact contact--right">
      <li class="contact__item">
        <svg class="contact__icon" viewBox="0 0 16 16"><circle cx="8" cy="8" r="7.5"/><g fill="none" stroke="#fff" stroke-width="1"><ellipse cx="8" cy="8" rx="3" ry="7"/><path d="M1 8h14M2 4.5h12M2 11.5h12"/></g></svg>
        <span>www.Brvenko.com</span>
      </li>
      <li class="contact__item">
        <svg class="contact__icon" viewBox="0 0 16 16"><path d="M8 0a5 5 0 0 0-5 5c0 4 5 9 5 9s5-5 5-9a5 5 0 0 0-5-5z"/><circle cx="8" cy="5" r="2" fill="#fff"/><rect x="4" y="15" width="8" height="1"/></svg>
        <span class="contact__company">BRVENKO LLC</span>
      </li>
      <li class="contact__item contact__indent">
        <span>4821 Mesquite Rd. Austin</span>
      </li>
    </ul>
  </section>

</div>
</body>
</html>
```